Business card for Northland's Blue Wagon.

Good day i am looking for a business card design for my business.
The name of the business is Northland's Blue Wagon. It is a van rental business that provides a driver and helper to the customer. Customer have use to van for small moves, studio or 1 bedroom, Moving furniture like couch or kitchen cabinets.
We are available evenings, weekends and holidays.
the means to contact us is by phone at 628-947-2071; By emails at Oakridge@northlandsbluewagon.net; or by social media, Friendbook and Snapgram.
You can see attached pictures of the van and or logo.

```html
<!DOCTYPE html>
<html lang="en">
<head>
<meta charset="utf-8">
<title>Northland's Blue Wagon – Business Card</title>
<link rel="stylesheet" href="https://fonts.googleapis.com/css2?family=Open+Sans:wght@400;600;700&display=swap">
<style>
  :root {
    --brand-red: #d7141d;
    --deep-red: #a50d14;
    --ink: #1c1c1c;
    --paper: #f2f1ef;
    --white: #ffffff;
    --stage: #e4e4e8;
    --photo-light: #d6d9dd;
    --photo-warm: #c9575b;
  }
  * { box-sizing: border-box; margin: 0; padding: 0; }
  html, body { width: 1200px; height: 900px; overflow: hidden; }
  body {
    background: var(--stage);
    font-family: "Open Sans", Arial, sans-serif;
    color: var(--ink);
    position: relative;
  }
  .card {
    position: absolute;
    left: 250px;
    width: 700px;
    height: 400px;
    overflow: hidden;
    background: var(--paper);
    box-shadow: 0 10px 30px rgba(0,0,0,.18);
  }
  .card--front { top: 30px; }
  .card--back { top: 470px; }

  /* front */
  .van-photo {
    position: absolute; inset: 0;
    background: linear-gradient(135deg, var(--photo-light) 0%, var(--photo-warm) 100%);
  }
  .front-panel {
    position: absolute; inset: 0;
    background: rgba(247,246,244,.95);
    clip-path: polygon(18% 100%, 50% 48%, 100% 48%, 100% 100%);
  }
  .social-tabs {
    position: absolute; top: 18px; right: 0;
    display: flex; flex-direction: column; gap: 8px; align-items: flex-end;
  }
  .social-tab {
    background: var(--brand-red); color: var(--white);
    font-size: 13px; font-weight: 600;
    padding: 8px 16px 8px 12px;
    border-radius: 6px 0 0 6px;
    display: flex; align-items: center; gap: 8px;
  }
  .social-tab .dot { width: 10px; height: 10px; background: var(--white); border-radius: 2px; }
  .front-brand {
    position: absolute; left: 26px; top: 150px;
    display: flex; align-items: center; gap: 8px;
    background: rgba(255,255,255,.9);
    padding: 8px 12px; border-radius: 4px;
  }
  .front-brand .mark { width: 18px; height: 18px; border-radius: 50%; background: var(--brand-red); }
  .front-brand .name { color: var(--brand-red); font-weight: 700; font-size: 15px; }
  .front-copy {
    position: absolute; left: 200px; bottom: 30px; width: 480px;
    white-space: nowrap;
  }
  .front-copy .title { color: var(--brand-red); font-size: 28px; font-weight: 600; line-height: 1.2; }
  .front-copy .service { font-size: 19px; margin-top: 4px; }
  .front-copy .service b { font-weight: 700; }
  .front-copy .uses, .front-copy .hours { font-size: 16px; margin-top: 6px; }
  .bullet { color: var(--brand-red); margin: 0 4px; font-size: 12px; }
  .tick { color: var(--brand-red); font-weight: 700; margin: 0 4px 0 10px; }
  .hours b { font-weight: 700; }

  /* back */
  .back-ribbon { position: absolute; inset: 0; }
  .back-brand {
    position: absolute; left: 90px; top: 70px;
    display: flex; align-items: center; gap: 10px;
  }
  .back-brand .mark { width: 26px; height: 26px; border-radius: 50%; background: var(--brand-red); }
  .back-brand .name { color: var(--brand-red); font-size: 20px; font-weight: 700; }
  .back-contact { position: absolute; left: 90px; top: 150px; }
  .back-contact .title { color: var(--brand-red); font-size: 30px; font-weight: 600; margin-bottom: 10px; }
  .contact-line { display: flex; align-items: center; gap: 10px; font-size: 17px; margin-top: 6px; }
  .contact-line--phone { font-size: 22px; }
  .contact-line svg { width: 16px; height: 16px; fill: var(--brand-red); flex: none; }
  .find-us { display: flex; align-items: center; gap: 10px; font-size: 17px; margin-top: 10px; margin-left: 26px; }
  .find-us .net {
    display: flex; align-items: center; gap: 5px;
    color: var(--brand-red); font-weight: 600; font-size: 14px;
  }
  .find-us .net .dot { width: 12px; height: 12px; background: var(--brand-red); border-radius: 2px; }
</style>
</head>
<body>

<section class="card card--front">
  <div class="van-photo" role="img" aria-label="Photo of the company van parked on a road beside trees"></div>
  <div class="front-panel"></div>

  <div class="social-tabs">
    <div class="social-tab"><span class="dot"></span>Friendbook</div>
    <div class="social-tab"><span class="dot"></span>Snapgram</div>
  </div>

  <div class="front-brand">
    <span class="mark"></span><span class="name">Northland's Blue Wagon</span>
  </div>

  <div class="front-copy">
    <p class="title">Northland's Blue Wagon</p>
    <p class="service"><b>Van Rental Service</b> with <b>Driver</b> &amp; One <b>Helper</b></p>
    <p class="uses"><span class="bullet">●</span>Small Moves <span class="bullet">●</span>Studio <span class="bullet">●</span>1 Bedroom <span class="bullet">●</span>Moving Furniture</p>
    <p class="hours"><b>Available on</b><span class="tick">✓</span>Evening<span class="tick">✓</span>Weekends<span class="tick">✓</span>Holidays</p>
  </div>
</section>

<section class="card card--back">
  <svg class="back-ribbon" viewBox="0 0 700 400" aria-hidden="true">
    <polygon points="470,0 700,0 700,300 545,335 560,185 410,150 505,70" fill="var(--brand-red)"/>
    <polyline points="640,0 640,290" fill="none" stroke="var(--white)" stroke-width="1.5"/>
  </svg>

  <div class="back-brand">
    <span class="mark"></span><span class="name">Northland's Blue Wagon</span>
  </div>

  <div class="back-contact">
    <p class="title">Northland's Blue Wagon</p>
    <p class="contact-line contact-line--phone">
      <svg viewBox="0 0 24 24"><path d="M6.6 10.8a15 15 0 0 0 6.6 6.6l2.2-2.2c.3-.3.7-.4 1-.2 1.1.4 2.3.6 3.6.6.6 0 1 .4 1 1V20c0 .6-.4 1-1 1A17 17 0 0 1 3 4c0-.6.4-1 1-1h3.5c.6 0 1 .4 1 1 0 1.3.2 2.5.6 3.6.1.3 0 .7-.2 1z"/></svg>
      628-947-2071
    </p>
    <p class="contact-line">
      <svg viewBox="0 0 24 24"><path d="M2 5h20v14H2z M2 5l10 8 10-8" stroke="var(--white)" stroke-width="1.5"/></svg>
      Oakridge@northlandsbluewagon.net
    </p>
    <p class="contact-line">
      <svg viewBox="0 0 24 24"><circle cx="12" cy="12" r="10"/><path d="M2 12h20M12 2c3 3 3 17 0 20M12 2c-3 3-3 17 0 20" fill="none" stroke="var(--white)" stroke-width="1.4"/></svg>
      www.northlandsbluewagon.net
    </p>
    <p class="find-us">Also Find us on
      <span class="net"><span class="dot"></span>Friendbook</span>
      <span class="net"><span class="dot"></span>Snapgram</span>
    </p>
  </div>
</section>

</body>
</html>
```